Modern Dental Appointment Reminder/Business Card

We already have a beautiful logo and icon picked from here on ArtisanHive, now we need someone to make them into a beautiful business card for us! This business card will also function as an appointment reminder card for patients. It will be double sided and must include:
Front
-Contact Info as Follows:
(Gavin R Moss, DDS
Family and Cosmetic Dentistry
2946 S 1320 E Ste 400
Larkfield, Vermont 84137)
-Our Logo or Icon (your choice, if Icon must write "Bellmere Dental" below it like in the example file)
Back
-"You're Invited!"
-"Your next appointment is on"
-Place to write date & time
-"Please call 24hrs ahead if appointment is to be cancelled
-Our Icon

Logo and Icon to be used are attached below, along with an example of what we need.
Please do NOT use lots of red! We want the red to just be an accent. Please use grey, white, or even a muted teal for the majority of the card.

Industry/Entity Type

Dentistry

Contact Information for Business Card

Gavin R Moss, DDS
2946 S 1320 E Ste 400
Larkfield, Vermont 84137

Colors
cfeae6

Requirements
Should not have
• Lots of red!

```html
<!DOCTYPE html>
<html lang="en">
<head>
<meta charset="utf-8">
<title>Bellmere Dental – Business &amp; Appointment Card</title>
<link rel="stylesheet" href="https://fonts.googleapis.com/css2?family=Cinzel:wght@600&family=Merriweather:ital,wght@0,400;0,700;0,900&family=Arimo:wght@400&display=swap">
<style>
  :root {
    --backdrop: #2e2e2e;
    --card: #ffffff;
    --red: #a4282c;
    --slate: #58544c;
    --ink: #4a4742;
    --muted: #6b6862;
    --rule: #9a9792;
  }
  * { box-sizing: border-box; margin: 0; padding: 0; }
  html, body { width: 1200px; height: 866px; overflow: hidden; background: var(--backdrop); }
  .sheet { position: relative; width: 1200px; height: 866px; }
  .card {
    position: absolute; top: 273px; width: 560px; height: 320px;
    background: var(--card); overflow: hidden;
    box-shadow: 0 6px 18px rgba(0,0,0,.45);
  }
  .card--front { left: 26px; }
  .card--back { left: 614px; }

  /* Front */
  .front__band { position: absolute; left: 0; bottom: 0; height: 14px; }
  .front__band--red { width: 46%; background: var(--red); height: 9px; }
  .front__band--slate { left: 46%; right: 0; background: var(--slate); }
  .brand { position: absolute; left: 262px; top: 64px; display: flex; align-items: center; gap: 14px; }
  .brand__dot { width: 64px; height: 64px; border-radius: 50%; background: var(--slate); flex: none; }
  .brand__name {
    font-family: "Cinzel", serif; font-weight: 600; color: var(--red);
    font-size: 30px; line-height: 1.05; letter-spacing: 1px;
  }
  .doctor { position: absolute; left: 30px; top: 150px; }
  .doctor__name { font-family: "Merriweather", serif; font-weight: 900; color: var(--red); font-size: 17px; letter-spacing: .5px; }
  .doctor__name span { font-weight: 400; color: var(--ink); font-size: 16px; }
  .doctor__field { font-family: "Arimo", sans-serif; color: var(--muted); font-size: 14px; margin-top: 4px; }
  .divider { position: absolute; left: 30px; right: 30px; height: 1px; background: var(--rule); top: 205px; }
  .address { position: absolute; right: 40px; top: 222px; display: flex; gap: 10px; align-items: flex-start; }
  .address__pin { width: 18px; height: 22px; flex: none; margin-top: 2px; }
  .address__lines { font-family: "Arimo", sans-serif; color: var(--ink); font-size: 16px; line-height: 1.35; }

  /* Back */
  .back__band { position: absolute; left: 0; top: 0; bottom: 0; width: 110px; background: var(--slate); }
  .back__square { position: absolute; left: 40px; top: 40px; width: 110px; height: 110px; background: var(--red); }
  .back__name {
    position: absolute; left: 124px; top: 164px; width: 80px;
    font-family: "Cinzel", serif; font-weight: 600; color: var(--red);
    font-size: 15px; line-height: 1.15;
  }
  .invite { position: absolute; left: 215px; top: 40px; right: 30px; }
  .invite__title { font-family: "Merriweather", serif; font-weight: 900; color: var(--red); font-size: 22px; letter-spacing: .5px; }
  .invite__lead { font-family: "Merriweather", serif; color: var(--ink); font-size: 16px; margin-top: 6px; }
  .field { display: flex; align-items: flex-end; gap: 8px; margin-top: 20px; font-family: "Arimo", sans-serif; color: var(--ink); font-size: 19px; }
  .field__line { flex: 1; height: 1px; background: var(--rule); margin-bottom: 4px; }
  .invite__note { font-family: "Arimo", sans-serif; color: var(--muted); font-size: 12.5px; line-height: 1.4; margin-top: 26px; }
</style>
</head>
<body>
<main class="sheet">
  <section class="card card--front" aria-label="Card front">
    <div class="brand">
      <div class="brand__dot"></div>
      <div class="brand__name">BELLMERE<br>DENTAL</div>
    </div>
    <div class="doctor">
      <p class="doctor__name">GAVIN R MOSS <span>DDS</span></p>
      <p class="doctor__field">Family and Cosmetic Dentistry</p>
    </div>
    <div class="divider"></div>
    <div class="address">
      <svg class="address__pin" viewBox="0 0 18 22" aria-hidden="true">
        <path d="M9 1a7.5 7.5 0 0 0-7.5 7.5C1.5 14 9 21 9 21s7.5-7 7.5-12.5A7.5 7.5 0 0 0 9 1z" fill="none" stroke="#a4282c" stroke-width="2"/>
        <circle cx="9" cy="8.5" r="2.6" fill="#a4282c"/>
      </svg>
      <p class="address__lines">2946 S 1320 E Ste 400<br>Larkfield, Vermont 84137</p>
    </div>
    <div class="front__band front__band--red"></div>
    <div class="front__band front__band--slate"></div>
  </section>

  <section class="card card--back" aria-label="Card back">
    <div class="back__band"></div>
    <div class="back__square"></div>
    <p class="back__name">BELLMERE<br>DENTAL</p>
    <div class="invite">
      <h1 class="invite__title">YOU'RE INVITED!</h1>
      <p class="invite__lead">Your next appointment is on</p>
      <div class="field"><span>TIME</span><span class="field__line"></span></div>
      <div class="field"><span>DATE</span><span class="field__line"></span></div>
      <p class="invite__note">Please call 24hrs ahead if appointment is<br>to be cancelled</p>
    </div>
  </section>
</main>
</body>
</html>
```